Naturopath Practitioner Card Design

I am a naturopath needing a design for a business card mainly to show that I am a naturopath and have some contact details to give to prospective clients. I am open minded about the design and what is on the second side of the card whether it just be some artwork or space for details, appointment times etc. Naturopathy is the practice of natural medicine that uses a holistic approach and incorporates herbal and nutritional medicine.

Industry/Entity Type

Business

Contact Information for Business Card

Tom Welby NaturopathBHSc (Naturopathy) Member PHRA 0492 815 306 tom.welby@mailbright.com www.tomwelbynaturopathy.com.au

Requirements
Nice to have
• Would prefer some kind of original pattern/art work/logo rather than an image, not fussed if its very simple/basic
• I am open to any colour but think I would prefer a more earthy sandy clay etc type style than the greens that are commonly associated with naturopathy.
Should not have
• Don't really want to have generic stock images on it

```html
<!DOCTYPE html>
<html lang="en">
<head>
<meta charset="utf-8">
<title>Tom Welby – Naturopath Business Card</title>
<link rel="stylesheet" href="https://fonts.googleapis.com/css2?family=Open+Sans:wght@400;700&display=swap">
<style>
  :root{
    --page:#d9d9db;
    --ink:#2b2b2b;
    --ink-soft:#444;
    --brand-blue:#1a6cc4;
    --white:#ffffff;
  }
  html,body{margin:0;padding:0;overflow:hidden;}
  body{
    width:1200px;height:880px;background:var(--page);
    display:flex;align-items:center;justify-content:center;gap:100px;
    font-family:"Open Sans",Arial,sans-serif;
  }
  .card{width:320px;height:560px;display:block;box-shadow:0 10px 28px rgba(0,0,0,.25);}
  .card__dark{fill:url(#darkField);}
  .card__light{fill:url(#lightField);}
  .card__panel{fill:url(#bluePanel);}
  .brand-name{font-family:"Open Sans",Arial,sans-serif;font-weight:400;font-size:19px;}
  .brand-name--front{fill:var(--brand-blue);}
  .brand-name--back{fill:var(--ink);}
  .brand-dot{fill:var(--brand-blue);}
  .person-name{font-weight:700;font-size:16px;fill:var(--ink);}
  .person-role{font-size:11px;fill:var(--ink-soft);}
  .icon-tile{fill:var(--white);}
  .icon{fill:var(--ink);}
  .contact{font-size:9.5px;fill:var(--white);}
</style>
</head>
<body>
<svg width="0" height="0" style="position:absolute" aria-hidden="true">
  <defs>
    <linearGradient id="darkField" x1="0" y1="0" x2="1" y2="1">
      <stop offset="0" stop-color="#2c2c2e"/><stop offset="1" stop-color="#1f1f21"/>
    </linearGradient>
    <linearGradient id="lightField" x1="0" y1="0" x2="1" y2="1">
      <stop offset="0" stop-color="#f0f0f0"/><stop offset=".5" stop-color="#dedede"/><stop offset="1" stop-color="#ebebeb"/>
    </linearGradient>
    <linearGradient id="bluePanel" x1="0" y1="0" x2="1" y2="1">
      <stop offset="0" stop-color="#1f74cc"/><stop offset="1" stop-color="#0f57a8"/>
    </linearGradient>
  </defs>
</svg>

<svg class="card card--front" viewBox="0 0 320 560" role="group" aria-label="Card front">
  <rect class="card__dark" width="320" height="560" role="img" aria-label="Dark faceted geometric background"/>
  <path class="card__light" role="img" aria-label="Light grey faceted geometric pattern"
        d="M40 0 H266 V200 L282 216 V560 H64 V410 L40 386 Z"/>
  <path class="card__panel" d="M64 506 a10 10 0 0 1 10 -10 H272 a10 10 0 0 1 10 10 V560 H64 Z"/>
  <circle class="brand-dot" cx="160" cy="300" r="13"/>
  <text class="brand-name brand-name--front" x="160" y="345" text-anchor="middle">Your Logo</text>
</svg>

<svg class="card card--back" viewBox="0 0 320 560" role="group" aria-label="Card back">
  <rect class="card__dark" width="320" height="560" role="img" aria-label="Dark faceted geometric background"/>
  <path class="card__light" role="img" aria-label="Light grey faceted geometric pattern"
        d="M54 0 H280 V170 L258 192 V560 H62 V220 L40 198 V14 Z"/>
  <rect class="card__panel" x="62" y="290" width="218" height="270" rx="10"/>
  <circle class="brand-dot" cx="160" cy="102" r="13"/>
  <text class="brand-name brand-name--back" x="160" y="146" text-anchor="middle">Your Logo</text>

  <text class="person-name" x="74" y="236">Tom Welby</text>
  <text class="person-role" x="74" y="254">NaturopathBHSc (Naturopathy)</text>
  <text class="person-role" x="74" y="271">Member PHRA0492 815</text>

  <rect class="icon-tile" x="48" y="322" width="28" height="28" rx="4"/>
  <path class="icon" d="M62 328 L70 336 H67 V344 H64 V339 H60 V344 H57 V336 H54 Z"/>
  <text class="contact" x="92" y="333">18 Harlow Street</text>
  <text class="contact" x="92" y="346">Tampa FL 33602</text>

  <rect class="icon-tile" x="48" y="378" width="28" height="28" rx="4"/>
  <path class="icon" d="M55 388 q7 -5 14 0 v3 h-3 v-2 q-4 -2 -8 0 v2 h-3 Z M56 392 h12 l1 8 h-14 Z"/>
  <text class="contact" x="92" y="389">555 . 2048 . 7316</text>
  <text class="contact" x="92" y="402">555 . 2048 . 7317</text>

  <rect class="icon-tile" x="48" y="434" width="28" height="28" rx="4"/>
  <path class="icon" d="M54 440 h16 v12 h-16 Z M56 442 v8 h12 v-8 Z M60 453 h4 v3 h3 v1 h-10 v-1 h3 Z"/>
  <text class="contact" x="92" y="445">306tom.welby@mailbright.com</text>
  <text class="contact" x="92" y="458">www.tomwelby.com</text>
</svg>
</body>
</html>
```